Pool Up, Pay Less! Innovative Team Buying Web App

Pooli is a team-buying/social commerce web app that is a cross between Bundlora and sites/apps like Kivo, Marlix, and Fenxiangtuo. It is basically like a game in which users seek to get the lowest prices by working with friends and neighbours (as a team) to maximize order volumes. Sellers on the platform set volume targets which teams have to hit to secure wholesale price.
We need a landing page and a few (4 - 5) key pages that project a compelling game-like aesthetic that is innovative and playful, while being clean and classy.

Target Market(s)

Nigerian homemakers. Typically 30+ years old. Predominantly female, middle class.

Industry/Entity Type

Ecommerce, Groceries.

Coding

Coded - Design and coding required

Number of Pages Required

5+ page

Requirements
Must have
• PAGES (1). Landing page. An attractive landing page that gives a brief overview of the concept and main features. We are going to roll out an MVP with just the landing page (which should include a sign-up form) so this page is critical and should be "self-contained" with it's signup inputs. The signup section must include a referral code so that we can track who referred whom. (2). Available deals. A listing of all active deals with enough relevant information. Note that deals have a deadline, a retail price, and a minimum volume target to unlock wholesale price. (3). Deal details page. This should show the standard price (the price the user would pay if he buys a small quantity), team price (the wholesale price based on the team hitting the required order volume), the points to be earned by buying the item, etc. (4). Checkout page. In addition to normal checkout stuff on this page the user can convert points into currency (at an exchange rate that may vary from time to time). Example: if price is $3,000 he may see that he has 1000 points in his wallet and the exchange rate is 1:1, so he can go ahead and convert to $1,000 and the price now becomes $2,000. (5). Profile page. Where the user can see things like his performance (how his points were calculated), his lineage ("children" and "grandchildren"), points required to get to the next rank, his order history, etc.
Nice to have
• GUIDELINES (1). Overall Aesthetic is game-like: playful, bright, and colourful. But clean and classic at the same time: we don't want a look that goes "out of fashion" within the next two or three years. (2). Referral is critical. Therefore the "Share" button (or whatever) should be easily accessible and visible on all relevant pages. (3). The user's community is critical. Therefore the activity of the users "network" (the "children" and "grandchildren") must be somehow dynamically visible at most/all times. We want to project a sense of realtime dynamism, just like a game. The user should be able to somehow "see" things happening in the network (e.g. when someone in his network buys something). (4). Like a game, the user's points, rank, and badges must always/usually be visible and we need an interesting visual effect when something happens that increases his points. Examples of actions that generate points include buying an item, when a "child" or "grandchild" buys an item, when someone you invited/referred creates an account, etc. We need a clear idea of the visual effect and how it would work.

```html
<!DOCTYPE html>
<html lang="en">
<head>
<meta charset="utf-8">
<title>Pooli — Checkout</title>
<link rel="stylesheet" href="https://fonts.googleapis.com/css2?family=Mulish:wght@400;600;700;800&display=swap">
<style>
  :root {
    --ink: #111111;
    --muted: #2b2b2b;
    --accent: #e3131b;
    --line: #e2e2e2;
    --field-line: #dcdcdc;
    --footer-bg: #262626;
    --footer-text: #dcdcdc;
    --footer-rule: #4a4a4a;
    --white: #ffffff;
    --photo-watch-a: #eceef2;
    --photo-watch-b: #f3dfa8;
    --photo-camera-a: #ececec;
    --photo-camera-b: #cfcfcf;
  }
  * { box-sizing: border-box; margin: 0; padding: 0; }
  html, body { width: 1200px; height: 1114px; overflow: hidden; }
  body {
    position: relative;
    background: var(--white);
    font-family: "Mulish", sans-serif;
    color: var(--ink);
  }
  .abs { position: absolute; }

  /* Header */
  .brand { left: 133px; top: 26px; font-size: 25px; font-weight: 800; letter-spacing: 0.5px; }
  .main-nav a {
    position: absolute; top: 31px; font-size: 14.5px; color: var(--ink);
    text-decoration: none; white-space: nowrap;
  }
  .login {
    left: 994px; top: 26px; width: 74px; height: 31px; border-radius: 16px;
    background: var(--accent); color: var(--white); font-size: 15px; font-weight: 600;
    display: flex; align-items: center; justify-content: center;
  }

  /* Cart items */
  .cart-item {
    position: absolute; left: 130px; width: 939px; height: 137px;
    border: 1px solid var(--line); border-radius: 8px;
  }
  .item-photo {
    position: absolute; left: 36px; top: 20px; width: 112px; height: 92px; border-radius: 6px;
  }
  .item-photo.watch { background: linear-gradient(135deg, var(--photo-watch-a), var(--photo-watch-b)); }
  .item-photo.camera { background: linear-gradient(135deg, var(--photo-camera-a), var(--photo-camera-b)); }
  .item-title { position: absolute; left: 191px; top: 22px; font-size: 13.5px; font-weight: 600; line-height: 19px; }
  .qty-label { position: absolute; left: 192px; top: 80px; font-size: 14px; color: var(--muted); }
  .qty-field {
    position: absolute; left: 229px; top: 72px; width: 44px; height: 34px;
    border: 1px solid var(--ink); border-radius: 6px;
    display: flex; align-items: center; justify-content: center; font-size: 13.5px;
  }
  .team-price { position: absolute; right: 32px; top: 32px; text-align: right; font-size: 14px; line-height: 23px; color: var(--muted); }
  .team-price .price { color: var(--accent); font-size: 14.5px; line-height: 27px; }

  /* Points conversion */
  .field-label { top: 421px; font-size: 16px; font-weight: 400; }
  .field-box {
    top: 451px; width: 122px; height: 46px; border: 1px solid var(--field-line); border-radius: 10px;
    padding-left: 16px; display: flex; align-items: center; font-size: 16px;
  }
  .swap-icon { left: 273px; top: 461px; }

  /* Summary */
  .summary-label { right: 275px; font-size: 16px; color: var(--muted); }
  .summary-value { right: 130px; font-size: 16px; font-weight: 700; }
  .summary-rule { left: 132px; top: 668px; width: 937px; height: 1px; background: var(--ink); }

  /* Footer */
  .footer-wave { left: 0; top: 730px; }
  .footer-brand { left: 135px; top: 912px; font-size: 25px; font-weight: 800; color: var(--white); letter-spacing: 0.5px; }
  .footer-col { top: 892px; }
  .footer-col h4 { font-size: 13px; font-weight: 800; color: var(--white); margin-bottom: 8px; }
  .footer-col a { display: block; font-size: 13px; line-height: 19.2px; color: var(--footer-text); text-decoration: none; white-space: nowrap; }
  .social { position: absolute; top: 923px; width: 25px; height: 25px; background: var(--white); }
  .footer-rule { left: 130px; top: 1040px; width: 940px; height: 1px; background: var(--footer-rule); }
  .copyright { left: 0; width: 1200px; top: 1076px; text-align: center; font-size: 12.5px; color: var(--white); }
</style>
</head>
<body>

<header>
  <div class="abs brand">POOLI</div>
  <nav class="main-nav">
    <a style="left:416px">Group Buying</a>
    <a style="left:539px">Group Donations</a>
    <a style="left:685px">Group Alarm</a>
    <a style="left:802px">Group Chat</a>
    <a style="left:914px">Visitors</a>
  </nav>
  <div class="abs login">Login</div>
</header>

<main>
  <article class="cart-item" style="top:94px">
    <div class="item-photo watch" role="img" aria-label="Product photo: wristwatch"></div>
    <p class="item-title">Lorem ipsum dolor sit amet, consectetur adipiscing elit<br>sed do eiusmod tempor incididunt</p>
    <span class="qty-label">Qty</span>
    <div class="qty-field">2</div>
    <div class="team-price">Team Price<br><span class="price">$256.00</span><br>20-99 pieces</div>
  </article>

  <article class="cart-item" style="top:246px">
    <div class="item-photo camera" role="img" aria-label="Product photo: video camcorder"></div>
    <p class="item-title">Lorem ipsum dolor sit amet, consectetur adipiscing elit<br>sed do eiusmod tempor incididunt</p>
    <span class="qty-label">Qty</span>
    <div class="qty-field">4</div>
    <div class="team-price">Team Price<br><span class="price">$500.00</span><br>20-99 pieces</div>
  </article>

  <section class="points-convert">
    <div class="abs field-label" style="left:131px">Points</div>
    <div class="abs field-box" style="left:131px">1000</div>
    <svg class="abs swap-icon" width="28" height="24" viewBox="0 0 28 24" fill="none" stroke="#111" stroke-width="1.8" stroke-linecap="round" aria-hidden="true">
      <path d="M2 9 H26 M2 9 L8 3"/>
      <path d="M26 15 H2 M26 15 L20 21"/>
    </svg>
    <div class="abs field-label" style="left:323px">Exchange Rate</div>
    <div class="abs field-box" style="left:323px">$100</div>
  </section>

  <section class="order-summary">
    <div class="abs summary-label" style="top:429px">Sub Total</div>
    <div class="abs summary-value" style="top:428px">$756.00</div>
    <div class="abs summary-label" style="top:485px">Tax (12%)</div>
    <div class="abs summary-value" style="top:484px">$20.00</div>
    <div class="abs summary-label" style="top:541px">Shipping</div>
    <div class="abs summary-value" style="top:540px">FREE</div>
    <div class="abs summary-label" style="top:597px">Points</div>
    <div class="abs summary-value" style="top:596px">$100.00</div>
    <div class="abs summary-rule"></div>
    <div class="abs summary-label" style="top:695px">Total</div>
    <div class="abs summary-value" style="top:689px">$676.00</div>
  </section>
</main>

<footer>
  <svg class="abs footer-wave" width="1200" height="384" viewBox="0 730 1200 384" aria-hidden="true">
    <path d="M0 822 C150 856 380 850 540 800 C680 757 900 740 1200 808 L1200 1114 L0 1114 Z" fill="var(--footer-bg)"/>
  </svg>
  <div class="abs footer-brand">POOLI</div>

  <div class="abs footer-col" style="left:302px">
    <h4>RESOURCES</h4>
    <a>Product support</a>
    <a>Request a demo</a>
    <a>Online Demos (Video)</a>
  </div>
  <div class="abs footer-col" style="left:564px">
    <h4>COMPANY</h4>
    <a>Contact us</a>
    <a>Legal</a>
  </div>
  <div class="abs footer-col" style="left:744px">
    <h4>MENU</h4>
    <a>Group Buying</a>
    <a>Group Donations</a>
    <a>Group Alarm</a>
    <a>Group Chat</a>
    <a>Visitors</a>
  </div>
  <div class="abs footer-col" style="left:932px">
    <h4>FOLLOW US</h4>
  </div>
  <span class="social" style="left:934px" aria-label="Social link"></span>
  <span class="social" style="left:971px" aria-label="Social link"></span>
  <span class="social" style="left:1008px" aria-label="Social link"></span>
  <span class="social" style="left:1044px" aria-label="Social link"></span>

  <div class="abs footer-rule"></div>
  <div class="abs copyright">Copyright © 2023 All Rights Reserved</div>
</footer>

</body>
</html>
```